Brantwell Group needs a business card design

We need a new business card design using the logo recently selected in a logo competition on Pixel Forum. Our business is a consultancy specializing in aviation and energy and the winning business card design will promote an image of precision and professionalism with creativity.

Please use the logo with the name on the front of the card and use a complementary font. Make the back white with either the light grey or dark grey logo.

Target Market(s)

Senior finance and legal leaders at aviation and energy companies

Industry/Entity Type

Management Consulting

Contact Information for Business Card

Peter Haldane
President
Brantwell Group

www.brantwellgroup.example

(555) 304-6198
ph@brantwellgroup.example

Requirements
Must have
• Professional font that goes well with the logo font

```html
<!DOCTYPE html>
<html lang="en">
<head>
<meta charset="utf-8">
<title>Brantwell Group — Business Card</title>
<link rel="stylesheet" href="https://fonts.googleapis.com/css2?family=Open+Sans:wght@400;600;700&display=swap">
<style>
  :root {
    --navy: #154675;
    --navy-text: #1c4a7a;
    --paper: #f4f4f5;
    --rule: #9a9ea4;
    --page: #e6e7e9;
    --white: #ffffff;
    --muted: #d6e0ea;
  }
  * { box-sizing: border-box; margin: 0; padding: 0; }
  html, body {
    width: 1200px; height: 900px; overflow: hidden;
    background: var(--page);
    font-family: "Open Sans", Arial, sans-serif;
  }
  .sheet {
    position: relative; width: 1200px; height: 900px;
  }
  .card {
    position: absolute; left: 290px;
    width: 620px; height: 354px;
    background: var(--paper);
    box-shadow: 0 4px 14px rgba(0,0,0,0.12);
    overflow: hidden;
  }
  .card--back { top: 70px; }
  .card--front { top: 476px; }

  .wordmark {
    position: absolute;
    display: flex; align-items: center; gap: 14px;
    color: var(--navy-text);
    font-weight: 600;
    text-transform: uppercase;
  }
  .wordmark__dot {
    width: 14px; height: 14px; background: var(--navy);
  }
  .wordmark__name { display: flex; flex-direction: column; line-height: 1; }
  .wordmark__line1 { font-size: 34px; letter-spacing: 2px; }
  .wordmark__line2 { font-size: 15px; letter-spacing: 12px; margin-top: 6px; text-align: center; }

  .card--back .wordmark { left: 330px; top: 176px; }
  .card--front .wordmark { left: 290px; top: 56px; }

  .band {
    position: absolute; left: 0; right: 0; top: 180px; bottom: 0;
    background: var(--navy);
  }
  .band__rule {
    position: absolute; left: 0; right: 0; top: 172px; height: 8px;
    background: var(--rule);
  }
  .band__notch {
    position: absolute; left: 110px; top: 180px;
    width: 0; height: 0;
    border-left: 7px solid transparent; border-right: 7px solid transparent;
    border-top: 8px solid var(--paper);
  }
  .holder {
    position: absolute; left: 40px; top: 200px; color: var(--white);
  }
  .holder__name { font-size: 17px; font-weight: 700; }
  .holder__title { font-size: 13px; font-weight: 400; margin-top: 4px; color: var(--muted); }

  .contacts {
    position: absolute; left: 300px; top: 206px;
    list-style: none; color: var(--white);
    font-size: 15px; font-weight: 400;
  }
  .contacts li { display: flex; align-items: center; gap: 14px; height: 30px; }
  .contacts svg { width: 16px; height: 16px; flex: none; }
</style>
</head>
<body>
<main class="sheet">
  <section class="card card--back" aria-label="Card back">
    <div class="wordmark">
      <span class="wordmark__dot"></span>
      <span class="wordmark__name"><span class="wordmark__line1">Brantwell</span><span class="wordmark__line2">Group</span></span>
    </div>
  </section>

  <section class="card card--front" aria-label="Card front">
    <div class="wordmark">
      <span class="wordmark__dot"></span>
      <span class="wordmark__name"><span class="wordmark__line1">Brantwell</span><span class="wordmark__line2">Group</span></span>
    </div>
    <div class="band__rule"></div>
    <div class="band"></div>
    <div class="band__notch"></div>
    <div class="holder">
      <p class="holder__name">Peter Haldane</p>
      <p class="holder__title">President</p>
    </div>
    <ul class="contacts">
      <li>
        <svg viewBox="0 0 16 16" aria-hidden="true"><path d="M2 5c0-2 2-3 6-3s6 1 6 3v1h-3V4.5H5V6H2z M4 8h8l2 5H2z" fill="#fff"/><circle cx="8" cy="10.5" r="1.6" fill="#154675"/></svg>
        <span>(555) 304-6198</span>
      </li>
      <li>
        <svg viewBox="0 0 16 16" aria-hidden="true"><rect x="1.5" y="3.5" width="13" height="9" fill="none" stroke="#fff" stroke-width="1.4"/><path d="M1.5 3.5 8 9l6.5-5.5" fill="none" stroke="#fff" stroke-width="1.4"/></svg>
        <span>ph@brantwellgroup.example</span>
      </li>
      <li>
        <svg viewBox="0 0 16 16" aria-hidden="true"><circle cx="8" cy="8" r="6.5" fill="none" stroke="#fff" stroke-width="1.4"/><ellipse cx="8" cy="8" rx="2.8" ry="6.5" fill="none" stroke="#fff" stroke-width="1.2"/><path d="M1.5 8h13" stroke="#fff" stroke-width="1.2"/></svg>
        <span>www.brantwellgroup.example</span>
      </li>
    </ul>
  </section>
</main>
</body>
</html>
```